Business card design needed

Front of Card:
I would like to have nearly 3/4 of the card from the top in a Pea Green Colour with the word 'Lanternway' written in a(Watermelon Red colour) in the font 'Viner Hand ITC'. Lanternway to be written within the Green colour of the card.

The lower 1/3 of the card I would like to have white with the words:
Home and Garden Styling smaller than the word Lanternway in Black in the font 'Batang', centred underneath the green section.

At the very bottom in one corner in smaller print I would like to have my contact phone number: Pip M:0427916604 and then the email address:
E: lanternwaystyling@brivomail.net.au on the other side.

Back of Card:
Back of Card to be White
On one side (Left)
I would like the Heading "Garden" in the same pea green colour as the front and in the Viner Hand ITC font. On the other half of the card I would like 'Home' in the Watermelon Red Colour (same as front colour) and in the font Viner Hand ITC.
Underneath these Headings I would like written in black and in Batang font the following list of services.

Garden Home
Garden Styling Interior Styling
Plant Selection Furniture Selection/Arrangement Garden Maintenance Setting Up Home (after move)
Hedging/Mowing Merchandise and Stylist for
Work w/Local Nurseries Marbeck and Hune

Industry/Entity Type

Business

Contact Information for Business Card

Lanternway
Home and Garden Styling
M: 0427916604 E: lanternwaystyling@brivomail.net.au

```html
<!DOCTYPE html>
<html lang="en">
<head>
<meta charset="utf-8">
<title>Lanternway – Home and Garden Styling business card</title>
<link rel="stylesheet" href="https://fonts.googleapis.com/css2?family=Caveat+Brush&family=Gowun+Batang&display=swap">
<style>
  :root {
    --pea-green: #1f7a36;
    --watermelon: #e8384f;
    --ink: #2b2b2b;
    --paper: #ffffff;
    --backdrop: #ebecec;
    --edge: #cfd1d1;
    --hand: "Caveat Brush", cursive;
    --serif: "Gowun Batang", serif;
  }
  * { box-sizing: border-box; margin: 0; padding: 0; }
  html, body {
    width: 1165px; height: 1200px; overflow: hidden;
    background: var(--backdrop);
  }
  .card {
    position: absolute;
    width: 881px; height: 489px;
    background: var(--paper);
    border: 1px solid var(--edge);
    overflow: hidden;
    font-family: var(--serif);
    color: var(--ink);
  }
  .card-front { left: 168px; top: 77px; }
  .card-back  { left: 175px; top: 623px; height: 488px; }
  .card-shapes { position: absolute; inset: 0; width: 100%; height: 100%; }

  .brand-name {
    position: absolute; left: 0; right: 0; top: 38px;
    text-align: center;
    font-family: var(--hand);
    font-size: 168px; line-height: 1;
    color: var(--watermelon);
  }
  .tagline {
    position: absolute; left: 0; right: 0; top: 298px;
    text-align: center;
    font-size: 60px; line-height: 1.1;
    letter-spacing: 0.5px;
  }
  .contact-line {
    position: absolute; left: 50px; right: 40px; top: 410px;
    display: flex; align-items: center; gap: 16px;
    font-size: 22px; white-space: nowrap;
  }
  .contact-item { display: inline-flex; align-items: center; gap: 5px; }
  .contact-icon { width: 20px; height: 20px; fill: none; stroke: var(--ink); stroke-width: 1.6; }

  .service-heading {
    position: absolute; top: 78px;
    font-family: var(--hand);
    font-size: 56px; line-height: 1;
  }
  .service-heading-garden { left: 92px; color: var(--pea-green); }
  .service-heading-home { left: 543px; color: var(--watermelon); }

  .service-list {
    position: absolute; top: 252px;
    list-style: none;
    font-size: 23px; line-height: 37px;
  }
  .service-list-garden { left: 70px; }
  .service-list-home { left: 446px; }
  .service-list li { position: relative; padding-left: 18px; }
  .service-list li::before {
    content: ""; position: absolute; left: 0; top: 16px;
    width: 7px; height: 7px; border-radius: 50%;
  }
  .service-list-garden li::before { background: var(--pea-green); }
  .service-list-home li::before { background: var(--watermelon); }
</style>
</head>
<body>

<section class="card card-front" aria-label="Card front">
  <svg class="card-shapes" viewBox="0 0 712 395" preserveAspectRatio="none" aria-hidden="true">
    <path fill="var(--pea-green)" d="M0,0 H712 V234 C610,242 490,238 380,222 C260,205 110,205 0,234 Z"/>
    <path fill="var(--paper)" d="M0,202 C100,158 250,168 365,210 C250,186 100,186 0,218 Z"/>
    <path fill="var(--watermelon)" d="M372,213 C480,230 620,218 712,166 V198 C620,232 480,234 372,213 Z"/>
  </svg>
  <h1 class="brand-name">Lanternway</h1>
  <p class="tagline">Home and Garden Styling</p>
  <p class="contact-line">
    <span class="contact-item">Pip</span>
    <span class="contact-item">
      <svg class="contact-icon" viewBox="0 0 20 20" aria-hidden="true"><path d="M5 2 L8 6 L6 8 C7 11 9 13 12 14 L14 12 L18 15 L16 18 C9 18 2 11 2 4 Z"/></svg>
      0427916604
    </span>
    <span class="contact-item">
      <svg class="contact-icon" viewBox="0 0 20 20" aria-hidden="true"><rect x="2" y="5" width="16" height="11"/><path d="M2 5 L10 11 L18 5"/></svg>
      lanternwaystyling@brivomail.net.au
    </span>
  </p>
</section>

<section class="card card-back" aria-label="Card back">
  <svg class="card-shapes" viewBox="0 0 712 395" preserveAspectRatio="none" aria-hidden="true">
    <path fill="var(--pea-green)" d="M0,160 C100,124 250,138 355,170 C240,150 100,152 0,194 Z"/>
    <path fill="var(--watermelon)" d="M385,148 C500,170 630,160 712,112 V136 C640,172 500,174 385,148 Z"/>
  </svg>
  <h2 class="service-heading service-heading-garden">Garden</h2>
  <h2 class="service-heading service-heading-home">Home</h2>
  <ul class="service-list service-list-garden">
    <li>Garden Styling</li>
    <li>Plant Selection</li>
    <li>Garden Maintenance</li>
    <li>Hedging/Mowing</li>
    <li>Work w/Local Nurseries</li>
  </ul>
  <ul class="service-list service-list-home">
    <li>Interior Styling</li>
    <li>Furniture Selection/Arrangement</li>
    <li>Setting Up Home (after move)</li>
    <li>Merchandise and Stylist<br>for Marbeck &amp; Hune</li>
  </ul>
</section>

</body>
</html>
```